Book Cover for: TITLE Mend the Quiet Hours SUBTITLE For partners who want to stay together

We need a full cover design for a book on relationships written by husband and wife team, Marla and Walter Dunmore, PhD. This book will offer hope for couples that are on the verge of breaking up but want to work things out and stay together. The theme is to teach couples about their own reactions to their partner, how moods affect a relationship, how to get creative to solving problems and how to have a good feeling towards your partner regardless of differences. This book is about hope. It is a positive look at relationships that feel hopeless.

Target Market(s)

Married or couples that are going through a difficult time and are considering splitting up due to, communication difficulties, addiction, affair. We imagine the book will appeal to women more than men but still want a cover that men would be comfortable picking up.

Colors

Designer to choose colors to be used in the design.

Requirements
Must have
• We want the cover to beautiful, intriguing, simple and uncomplicated. We don't want it overly busy, technical, or complex.
Nice to have
• MAYBE?? a broken heart being put back together.
Should not have
• No photo, no cartoon, no flowers, no couple (unless obscure and not gender specific).

```html
<!DOCTYPE html>
<html lang="en">
<head>
<meta charset="utf-8">
<title>Mend the Quiet Hours — Full Cover</title>
<link rel="stylesheet" href="https://fonts.googleapis.com/css2?family=Montserrat:wght@600;700;800&family=Lato:wght@400;700&display=swap">
<style>
  :root {
    --stage: #3a3a3a;
    --paper: #d1d7cb;
    --sage: #7e8776;
    --chalk: #fbfbf7;
    --bronze: #b08a52;
    --ink: #1f1f1f;
    --heart: #d8232a;
    --hand: #c9c6c2;
  }
  * { margin: 0; padding: 0; box-sizing: border-box; }
  html, body { width: 1200px; height: 710px; overflow: hidden; background: var(--stage); }
  .cover {
    position: absolute; left: 129px; top: 20px;
    width: 941px; height: 670px;
    background: var(--paper);
    font-family: "Montserrat", sans-serif;
  }
  /* back cover */
  .back { position: absolute; left: 0; top: 0; width: 440px; height: 670px; }
  .back-title {
    position: absolute; left: 40px; top: 62px; width: 368px;
    font-weight: 800; font-size: 23.5px; color: var(--sage); letter-spacing: 0.2px; white-space: nowrap;
  }
  .back-title .accent, .front-title .accent, .spine-title .accent { color: var(--chalk); }
  .blurb, .bio {
    position: absolute; left: 40px; width: 368px;
    font-family: "Lato", sans-serif; font-size: 9.1px; line-height: 14.4px; color: var(--ink);
    text-align: justify;
  }
  .blurb { top: 98px; }
  .bio { top: 347px; }
  .blurb p, .bio p { margin-bottom: 14.4px; }
  .bio strong { font-weight: 700; }
  .bio .link { text-align: left; }
  .back-tagline {
    position: absolute; left: 40px; top: 286px; width: 368px; text-align: center;
    font-weight: 700; font-size: 18px; line-height: 27px; letter-spacing: 2.4px;
  }
  .tag-lead { color: var(--bronze); }
  .tag-rest { color: var(--sage); }
  /* spine */
  .spine { position: absolute; left: 440px; top: 0; width: 58px; height: 670px; }
  .spine-text {
    position: absolute; left: 50%; top: 33px;
    writing-mode: vertical-rl; transform: translateX(-50%);
    white-space: nowrap;
  }
  .spine-title { font-weight: 800; font-size: 25px; color: var(--sage); letter-spacing: 1.4px; }
  .spine-author {
    position: absolute; left: 50%; top: 423px; transform: translateX(-50%);
    writing-mode: vertical-rl; white-space: nowrap;
    font-weight: 700; font-size: 9.6px; color: var(--bronze); letter-spacing: 0.3px;
  }
  /* front cover */
  .front { position: absolute; left: 498px; top: 0; width: 443px; height: 670px; }
  .front-title {
    position: absolute; left: 0; top: 52px; width: 443px; text-align: center;
    font-weight: 800; color: var(--sage); line-height: 1;
  }
  .front-title span { display: block; }
  .line-one { font-size: 66px; margin-bottom: 16px; }
  .line-two { font-size: 78px; margin-bottom: 10px; }
  .line-three { font-size: 104px; }
  .artwork {
    position: absolute; left: 0; top: 362px; width: 443px; height: 134px;
    background: radial-gradient(ellipse 16% 46% at 50% 52%, var(--heart) 0%, var(--heart) 55%, rgba(201,198,194,0.9) 80%, rgba(201,198,194,0) 100%),
                linear-gradient(90deg, rgba(201,198,194,0.95) 0%, rgba(201,198,194,0.55) 38%, rgba(201,198,194,0.55) 62%, rgba(201,198,194,0.95) 100%);
  }
  .front-tagline {
    position: absolute; left: 0; top: 522px; width: 443px; text-align: center;
    font-weight: 700; letter-spacing: 2.6px;
  }
  .front-tagline .tag-lead { display: block; font-size: 19px; line-height: 30px; }
  .front-tagline .tag-rest { display: block; font-size: 18.5px; line-height: 34px; }
  .front-author {
    position: absolute; left: 0; top: 612px; width: 443px; text-align: center;
    font-weight: 700; font-size: 11.5px; color: var(--bronze); letter-spacing: 1.6px;
  }
</style>
</head>
<body>
  <main class="cover">
    <section class="back">
      <h2 class="back-title">MEND THE QUIET <span class="accent">HOURS</span></h2>
      <div class="blurb">
        <p>Have you ever wondered how you can go from being so deeply in love with your partner to finding yourself miserable in your relationship? What happened? This book sheds light on that question and the human dilemma around relationships. Marla and Walter Dunmore Ph.D. have been married for forty-five years and found their way out of their own troubled relationship. In this book, they propose a new approach that helps you live more gracefully with your partner’s flaws which allows you to put issues to rest, resolve differences, and move forward in your relationship with renewed love and commitment.</p>
        <p>Broken up into an easy, digestible format that includes real client vignettes and success stories, this book is essential for the struggling couple and has the potential to lead to a fresh start even when you have lost all hope.</p>
      </div>
      <div class="back-tagline">
        <span class="tag-lead">FOR PARTNERS WHO</span><br>
        <span class="tag-rest">WANT TO STAY TOGETHER</span>
      </div>
      <div class="bio">
        <p><strong>Marla and Walter Dunmore Ph.D.</strong> have been working with couples for several decades with an incredible success rate. They are co-partners at Dunmore and Associates, an educational organization in the Pacific Northwest, which provides consulting services for individuals, couples, parents, as well as leadership training for businesses and organizations.</p>
        <p>They have the same objective for everyone they work with; to help people have more hope and fulfillment in their lives, as well as function more synergistically. The diversity of Dunmore and Associates clientele is attributed to their unique understanding of human functioning and interaction, the application of which has significant impact on interpersonal relationships.</p>
        <p>They have curated a selection of recordings and books over the years to restore the good feeling between you and your partner. Their previous book, The Kinder Marriage Guide, is packed full of wisdom and practical perspective shifts that has the potential to change any relationship.</p>
        <p class="link">Learn more at www.dunmoreassociates.com.</p>
      </div>
    </section>

    <section class="spine">
      <div class="spine-text spine-title">MEND THE QUIET <span class="accent">HOURS</span></div>
      <div class="spine-author">MARLA AND WALTER DUNMORE, PHD</div>
    </section>

    <section class="front">
      <h1 class="front-title">
        <span class="line-one">MEND THE</span>
        <span class="line-two">QUIET</span>
        <span class="line-three accent">HOURS</span>
      </h1>
      <div class="artwork" role="img" aria-label="Two hands reaching in from either side, holding together the halves of a torn red paper heart joined with a bandage"></div>
      <div class="front-tagline">
        <span class="tag-lead">FOR PARTNERS WHO</span>
        <span class="tag-rest">WANT TO STAY TOGETHER</span>
      </div>
      <div class="front-author">MARLA AND WALTER DUNMORE, PHD</div>
    </section>
  </main>
</body>
</html>
```